Verdano TxRL PowerPoint Template

Template in Powerpoint 2010 format
The template is for Verdano Management Consultants, a firm based in Calgary, Alberta, Canada. For more information on Verdano, see www.verdano-example.ca
The PowerPoint presentation will be used for yearly events called TORL (Charting Our Fieldwork) and TYRL (Charting Your Fieldwork). At these one-day conferences, Verdano shares expertise/knowledge in current oil and gas technology solutions. Topics covered include: Who are the vendors? What are their products? What are their relative strengths and weaknesses? and What trends do we see?
We intend to use the template for several years. As a result, we would like the title to be dynamic, that is, changed each year to reflect the passing of time as new events are held (for example, TYRL 2013, TYRL 2014).
Verdano conducts almost all of its business in downtown Calgary for white collar clients. Our clients are primarily upstream Oil and Gas companies. Event attendees are typically business facing IT resources or business people with IT solutions responsibilities. In otherwords, we are communicating to a corporate audience.
The presentations for TYRL and TORL are compiled by multiple teams and are then merged together. As a result, previous presentations have looked unprofessional with inconsistent graphics, logos, fonts, font sizes, colours, etc. Team members using the new PowerPoint template will require guidance (within the template) on how to use it properly to provide a common look.
An example of a powerpoint presentation for a previous TYRL event that was designed in-house is attached for your reference.
Desired master slides for new PowerPoint template:
- Overall Session - Title Slide
- Functional Area – Title slide
- Content slides, including title with content, comparison, picture with caption
- Predictions slide
- Thank you slide
Desired outcome:
- a fresh, professional looking design
- a consistent look and feel across the slide-deck
- a user-friendly template/master slides
Additional concepts that COULD be incorporated:
- upstream onshore oil and gas graphics
- technology or software
NOTE: GIF and JPG versions of the VMC logo are attached. The logo colours are Blue – Pantone 288, and Yellow – Pantone 129

```html
<!DOCTYPE html>
<html lang="en">
<head>
<meta charset="utf-8">
<title>Verdano – Content Slide</title>
<link rel="stylesheet" href="https://fonts.googleapis.com/css2?family=Carlito:wght@400;700&family=Open+Sans:wght@400;600&display=swap">
<style>
  :root {
    --brand-blue: #1e3d98;
    --body-grey: #555a60;
    --muted-grey: #7a7d80;
    --rule-grey: #d6d8da;
    --paper: #ffffff;
    --mist: #eceef0;
    --badge-ink: #1c1c1c;
    --placeholder-tone: #c9d6df;
  }
  * { margin: 0; padding: 0; box-sizing: border-box; }
  html, body { width: 1200px; height: 900px; overflow: hidden; background: var(--paper); }
  .slide {
    position: relative;
    width: 1200px;
    height: 900px;
    overflow: hidden;
    background: radial-gradient(ellipse at 70% 20%, #ffffff 0%, #f6f7f8 55%, var(--mist) 100%);
    font-family: "Open Sans", Arial, sans-serif;
  }
  .slide__swoosh { position: absolute; inset: 0; }
  .slide__title {
    position: absolute; left: 57px; top: 50px;
    font-family: "Carlito", Calibri, sans-serif; font-weight: 400;
    font-size: 43px; color: var(--brand-blue); letter-spacing: 0.2px;
  }
  .event-badge { position: absolute; left: 1090px; top: 0; width: 78px; height: 108px; }
  .column-heading {
    position: absolute;
    font-family: "Carlito", Calibri, sans-serif; font-weight: 700;
    font-size: 34px; color: var(--brand-blue);
  }
  .column-heading--left { left: 57px; top: 158px; }
  .column-heading--right { left: 645px; top: 161px; }
  .feature-photo {
    position: absolute; left: 57px; top: 220px; width: 504px; height: 224px;
    border-radius: 8px; border: 3px solid #f2f3f4;
    box-shadow: 0 2px 6px rgba(0,0,0,0.25);
    background: var(--placeholder-tone);
  }
  .body-copy {
    position: absolute; font-size: 22.5px; line-height: 36px;
    color: var(--body-grey);
  }
  .body-copy__line {
    display: block; white-space: nowrap;
    text-align: justify; text-align-last: justify;
  }
  .body-copy__line--last { text-align: left; text-align-last: left; }
  .body-copy--left { left: 60px; top: 463px; width: 506px; }
  .body-copy--right { left: 645px; top: 218px; width: 506px; }
  .column-divider {
    position: absolute; left: 603px; top: 195px; width: 3px; height: 555px;
    background: linear-gradient(180deg, rgba(150,155,160,0) 0%, rgba(150,155,160,0.7) 25%, rgba(150,155,160,0.55) 75%, rgba(150,155,160,0) 100%);
  }
  .footer-rule { position: absolute; left: 0; top: 833px; width: 1200px; height: 2px; background: var(--rule-grey); }
  .brand-mark {
    position: absolute; left: 40px; top: 820px;
    display: flex; align-items: center; gap: 10px;
    background: var(--paper); padding: 6px 10px 6px 0;
  }
  .brand-mark__dot { width: 22px; height: 22px; border-radius: 50%; background: var(--brand-blue); }
  .brand-mark__name {
    font-family: "Carlito", Calibri, sans-serif; font-weight: 700;
    font-size: 38px; color: var(--brand-blue); letter-spacing: 1px;
  }
  .page-number {
    position: absolute; right: 30px; top: 848px;
    font-family: "Carlito", Calibri, sans-serif; font-weight: 700;
    font-size: 23px; color: var(--muted-grey);
  }
</style>
</head>
<body>
<main class="slide">
  <svg class="slide__swoosh" width="1200" height="900" viewBox="0 0 1200 900" aria-hidden="true">
    <path d="M300 0 C520 120 760 90 1200 30 L1200 0 Z" fill="#ffffff" opacity="0.7"/>
    <path d="M250 30 C520 160 860 140 1200 80" fill="none" stroke="#ffffff" stroke-width="18" opacity="0.8"/>
    <path d="M420 0 C620 200 900 300 1200 230" fill="none" stroke="#e9ebed" stroke-width="26" opacity="0.45"/>
    <path d="M700 520 C860 600 1000 760 1200 720" fill="none" stroke="#eaecee" stroke-width="34" opacity="0.4"/>
    <path d="M600 880 C800 760 1000 700 1200 780" fill="none" stroke="#ffffff" stroke-width="24" opacity="0.8"/>
  </svg>

  <h1 class="slide__title">Heading Here</h1>

  <svg class="event-badge" viewBox="0 0 78 108" role="img" aria-label="Event emblem">
    <path d="M2 0 H76 V88 L39 106 L2 88 Z" fill="#ffffff" stroke="#d0d2d4" stroke-width="1.5"/>
    <rect x="18" y="12" width="42" height="66" rx="3" fill="var(--badge-ink)"/>
  </svg>

  <h2 class="column-heading column-heading--left">Heading 4</h2>
  <h2 class="column-heading column-heading--right">Heading 5</h2>

  <div class="feature-photo" role="img" aria-label="Photo: cupped hands holding a small tree against sky and field"></div>

  <p class="body-copy body-copy--left">
    <span class="body-copy__line">Lorem ipsum dolor sit ipsum Lorem ipsum</span>
    <span class="body-copy__line">dolor sit ipsum Lorem ipsum dolor sit ipsum</span>
    <span class="body-copy__line">Lorem ipsum dolor sit ipsum Lorem ipsum</span>
    <span class="body-copy__line">dolor sit ipsum Lorem ipsum dolor sit ipsum</span>
    <span class="body-copy__line">Lorem ipsum dolor sit ipsum Lorem ipsum</span>
    <span class="body-copy__line body-copy__line--last">dolor sit ipsum Lorem ipsum</span>
  </p>

  <div class="column-divider"></div>

  <p class="body-copy body-copy--right">
    <span class="body-copy__line">Lorem ipsum dolor sit ipsum Lorem ipsum</span>
    <span class="body-copy__line">dolor sit ipsum Lorem ipsum dolor sit ipsum</span>
    <span class="body-copy__line">Lorem ipsum dolor sit ipsum Lorem ipsum</span>
    <span class="body-copy__line">dolor sit ipsum Lorem ipsum dolor sit ipsum</span>
    <span class="body-copy__line">Lorem ipsum dolor sit ipsum Lorem ipsum</span>
    <span class="body-copy__line">dolor sit ipsum Lorem ipsum dolor sit ipsum</span>
    <span class="body-copy__line">Lorem ipsum dolor sit ipsum Lorem ipsum</span>
    <span class="body-copy__line">dolor sit ipsum Lorem ipsum dolor sit ipsum</span>
    <span class="body-copy__line">Lorem ipsum dolor sit ipsum Lorem ipsum</span>
    <span class="body-copy__line">dolor sit ipsum Lorem ipsum dolor sit ipsum</span>
    <span class="body-copy__line">Lorem ipsum dolor sit ipsum Lorem ipsum</span>
    <span class="body-copy__line">dolor sit ipsum Lorem ipsum dolor sit ipsum</span>
    <span class="body-copy__line body-copy__line--last">Lorem ipsum dolor sit</span>
  </p>

  <div class="footer-rule"></div>

  <div class="brand-mark">
    <span class="brand-mark__dot"></span>
    <span class="brand-mark__name">VERDANO</span>
  </div>

  <div class="page-number">Page no. 01</div>
</main>
</body>
</html>
```